Flickora Channel Design

Create the design and layout for a new feature we are implementing in Flickora called channels. These channels will be for example: 48317, Keeper of the Ashes, Court of Falcons, and etc. These channels will allow people to join the channel and discuss freely about the channel specifically.

Flickora is the app, it is free to download. Download the app and go to messaging and this is where the channels are going to lay. We need what the screen is going to look like within our color scheme, but also once you join the channel how are the messages going to look. I sent a few examples below of what ScreenLog uses and Chatterly Uses. I want ours to look way better. I would like to see designs for our new feature we are looking to launch with channels for movies and shows. Users can join these channels and join in on the conversation.

Industry/Entity Type

Moves and Shows

Requirements
Nice to have
• Follow my color scheme that is already in place on Flickora app. Download Flickora on the app store.

```html
<!DOCTYPE html>
<html lang="en">
<head>
<meta charset="utf-8">
<title>Flickora — Channels App Design</title>
<link rel="stylesheet" href="https://fonts.googleapis.com/css2?family=Poppins:wght@400;500;600;700;800&display=swap">
<style>
  :root{
    --blue:#1f7fa8;
    --blue-dark:#186a8d;
    --orange:#fc5a16;
    --ink:#1c1c1c;
    --muted:#8c8c8c;
    --line:#e3e6ea;
    --aqua:#d2f7fb;
    --peach:#fdf1ea;
    --bg:#ffffff;
  }
  *{box-sizing:border-box;margin:0;padding:0}
  html,body{width:1200px;height:1200px;overflow:hidden}
  body{background:var(--bg);font-family:"Poppins",sans-serif;color:var(--ink);position:relative}

  /* brand block */
  .brand{position:absolute;left:124px;top:160px;width:180px;text-align:center}
  .brand-tile{width:154px;height:124px;margin:0 auto;border-radius:0 0 26px 26px;
    background:linear-gradient(#fff 10%,var(--aqua));display:flex;align-items:center;justify-content:center}
  .brand-tile span{width:26px;height:26px;border-radius:50%;background:var(--blue)}
  .brand-name{margin-top:18px;font-family:"Poppins",sans-serif;font-weight:800;font-size:38px;line-height:1;color:var(--blue);letter-spacing:.5px;white-space:nowrap}
  .brand-tag{margin:16px auto 0;width:158px;border:2px solid var(--orange);color:var(--orange);white-space:nowrap;
    font-weight:600;font-size:12px;letter-spacing:5.5px;padding:3px 0 3px 5.5px;line-height:1.3}

  /* screen labels */
  .screen-label{position:absolute;writing-mode:vertical-rl;transform:rotate(180deg);
    color:var(--blue);font-weight:600;font-size:10px;letter-spacing:6.5px;white-space:nowrap}

  /* phone screen */
  .screen{position:absolute;top:590px;width:240px;height:520px;background:#fff;border-radius:28px;
    overflow:hidden;border:1px solid var(--line);box-shadow:0 6px 20px rgba(20,60,80,.08)}
  .status{height:34px;display:flex;align-items:center;justify-content:space-between;padding:4px 22px 0 28px;font-size:10px;font-weight:600}
  .status-icons{display:flex;gap:4px;align-items:center}
  .body{display:flex;height:440px}
  .rail{width:46px;flex:none;background:linear-gradient(#fff 30%,var(--aqua));display:flex;flex-direction:column;align-items:center;gap:8px;padding-top:4px;position:relative}
  .rail-item{width:26px;height:26px;border-radius:50%;flex:none;position:relative}
  .rail-item.chat{background:#fff;box-shadow:0 1px 4px rgba(0,0,0,.15);display:flex;align-items:center;justify-content:center}
  .rail-item.chat.is-active{border-radius:8px;background:var(--blue)}
  .rail-item.chat::after{content:"";width:12px;height:11px;border-radius:50% 50% 50% 2px;background:var(--blue)}
  .rail-item.chat.is-active::after{background:#fff}
  .rail-item.is-active::before{content:"";position:absolute;left:-10px;top:4px;width:3px;height:18px;background:var(--orange);border-radius:2px}
  .poster-a{background:radial-gradient(circle at 50% 55%,#c8322a 35%,#1d1d1d 38%)}
  .poster-b{background:linear-gradient(#3c4a5c,#1f2734 60%,#c9b23a)}
  .poster-c{background:linear-gradient(135deg,#7b4a8a,#c98a3a 60%,#2e3a6b)}
  .poster-d{background:linear-gradient(#b8c2c8,#6e7a80 60%,#3e464b)}
  .rail-add{width:26px;height:26px;border-radius:50%;background:#fff;box-shadow:0 1px 4px rgba(0,0,0,.12);
    color:var(--blue);font-size:18px;line-height:25px;text-align:center;font-weight:300;margin-top:6px}

  .panel{flex:1;background:#fff;border-radius:12px 0 0 0;box-shadow:-2px 0 8px rgba(0,0,0,.05);padding:12px 8px 0 9px;overflow:hidden;position:relative}
  .panel-title{font-size:12px;font-weight:700;display:flex;justify-content:space-between;align-items:center;padding-right:4px}
  .dots{font-size:11px;font-weight:700;line-height:1}
  .search-row{display:flex;gap:6px;align-items:center;margin-top:8px}
  .search{flex:1;height:17px;border:1px solid var(--line);border-radius:9px;font-size:6.5px;color:#a8a8a8;display:flex;align-items:center;gap:5px;padding-left:8px}
  .add-member{width:16px;height:16px;border-radius:50%;background:#eceef1;flex:none;display:flex;align-items:center;justify-content:center}

  /* messages list */
  .thread-list{list-style:none;margin-top:10px}
  .thread{display:flex;gap:6px;align-items:center;height:29.5px;padding:0 4px;margin-left:-4px;margin-right:-4px}
  .thread.is-open{background:var(--peach);border-radius:4px}
  .avatar{width:20px;height:20px;border-radius:50%;flex:none;background:linear-gradient(135deg,#b9b9b9,#444)}
  .thread-text{flex:1;min-width:0}
  .thread-top{display:flex;justify-content:space-between;font-size:6px;color:var(--muted)}
  .thread-top b{font-weight:400}
  .thread-msg{font-size:4.6px;color:var(--muted);white-space:nowrap;overflow:hidden;text-overflow:ellipsis;margin-top:1px;display:flex;justify-content:space-between}
  .thread.is-unread .thread-top,.thread.is-unread .thread-msg{color:var(--ink);font-weight:600}
  .thread.is-unread .thread-top b{font-weight:600}
  .unread{width:4px;height:4px;border-radius:50%;background:var(--orange);flex:none;margin-left:4px}

  /* channels */
  .banner{border-radius:4px;background:linear-gradient(#8da4b4,#4e6070 55%,#2a3038);margin-top:10px}
  .banner-full{margin:-12px -8px 0 -9px;height:88px;background:linear-gradient(#8da4b4,#4e6070 55%,#2a3038)}
  .group{margin-top:12px}
  .group-head{font-size:5.5px;color:#444;letter-spacing:.2px;display:flex;align-items:center;gap:3px;margin-bottom:4px}
  .group-head::after{content:"";width:3px;height:3px;border-left:1px solid var(--orange);border-top:1px solid var(--orange);transform:rotate(45deg);margin-top:2px}
  .channel{font-size:6.5px;height:16.5px;display:flex;align-items:center;gap:5px;color:#222}
  .hash{color:var(--blue);font-weight:700;font-size:8px;width:6px}
  .ico-tri{width:0;height:0;border-left:3.5px solid transparent;border-right:3.5px solid transparent;border-bottom:6px solid var(--blue)}
  .ico-dot{width:6px;height:6px;border-radius:50%;background:var(--blue)}
  .ico-vol{width:6px;height:6px;background:var(--blue);clip-path:polygon(0 30%,35% 30%,80% 0,80% 100%,35% 70%,0 70%)}

  .fab{position:absolute;right:8px;bottom:10px;width:25px;height:25px;border-radius:50%;background:var(--orange);
    box-shadow:0 2px 6px rgba(252,90,22,.4);display:flex;align-items:center;justify-content:center}

  .nav{height:46px;border-top:1px solid #fde0cf;position:relative}
  .nav-icons{display:flex;justify-content:space-around;padding:8px 12px 0}
  .nav-icons svg{width:11px;height:11px}
  .nav-active-mark{position:absolute;top:-1px;left:56px;width:14px;height:2px;background:var(--orange)}
  .home-bar{position:absolute;left:50%;bottom:7px;width:80px;height:3px;border-radius:2px;background:#111;transform:translateX(-50%)}
</style>
</head>
<body>

<section class="brand">
  <div class="brand-tile"><span></span></div>
  <div class="brand-name">Flickora</div>
  <div class="brand-tag">APP DESIGN</div>
</section>

<!-- MESSAGES SCREEN -->
<div class="screen-label" style="left:166px;top:864px">MESSAGES SCREEN</div>
<article class="screen" style="left:196px">
  <div class="status"><span>9:41</span>
    <span class="status-icons"><svg width="11" height="7"><rect x="0" y="5" width="2" height="2"/><rect x="3" y="3.5" width="2" height="3.5"/><rect x="6" y="2" width="2" height="5"/><rect x="9" y="0" width="2" height="7"/></svg><svg width="9" height="7"><path d="M0.5 2.5a6 6 0 0 1 8 0M2 4a4 4 0 0 1 5 0M3.5 5.5a1.6 1.6 0 0 1 2 0" stroke="#000" fill="none" stroke-width="1.1"/></svg><svg width="14" height="7"><rect x=".5" y=".5" width="12" height="6" rx="1.5" fill="none" stroke="#999"/><rect x="1.5" y="1.5" width="10" height="4" rx="1"/></svg></span></div>
  <div class="body">
    <nav class="rail">
      <div class="rail-item chat is-active"></div>
      <div class="rail-item poster-a" role="img" aria-label="Channel poster: masked hero"></div>
      <div class="rail-item poster-b" role="img" aria-label="Channel poster: police comedy cast"></div>
      <div class="rail-item poster-c" role="img" aria-label="Channel poster: fantasy series"></div>
      <div class="rail-item poster-d" role="img" aria-label="Channel poster: city drama"></div>
      <div class="rail-add">+</div>
    </nav>
    <main class="panel">
      <h1 class="panel-title">Messages</h1>
      <div class="search-row"><div class="search"><svg width="6" height="6"><circle cx="2.5" cy="2.5" r="2" stroke="#666" fill="none"/><path d="M4 4l2 2" stroke="#666"/></svg>Search</div></div>
      <ul class="thread-list">
        <li class="thread is-unread"><span class="avatar"></span><div class="thread-text"><div class="thread-top"><b>AliceNneverland</b><span>2m ago</span></div><div class="thread-msg"><span>That was awesome!</span><i class="unread"></i></div></div></li>
        <li class="thread"><span class="avatar"></span><div class="thread-text"><div class="thread-top"><b>Elijah1980</b><span>10:16 AM</span></div><div class="thread-msg"><span>I definitely like it. HBU?</span></div></div></li>
        <li class="thread is-unread is-open"><span class="avatar"></span><div class="thread-text"><div class="thread-top"><b>Taylor13</b><span>12:13 PM</span></div><div class="thread-msg"><span>I think I've seen this film before and I didn't li...</span><i class="unread"></i></div></div></li>
        <li class="thread"><span class="avatar"></span><div class="thread-text"><div class="thread-top"><b>thatunknownguy</b><span>Jan 3</span></div><div class="thread-msg"><span>No problem</span></div></div></li>
        <li class="thread"><span class="avatar"></span><div class="thread-text"><div class="thread-top"><b>Alexandra_md</b><span>Jan 2</span></div><div class="thread-msg"><span>Agree! totally one of my favorite movies of all time</span></div></div></li>
        <li class="thread is-unread"><span class="avatar"></span><div class="thread-text"><div class="thread-top"><b>Cedric.cool</b><span>Jan 5</span></div><div class="thread-msg"><span>Wow</span><i class="unread"></i></div></div></li>
        <li class="thread"><span class="avatar"></span><div class="thread-text"><div class="thread-top"><b>spencer.wright</b><span>Jan 1</span></div><div class="thread-msg"><span>the visual effects are so impressive not gonna lie</span></div></div></li>
        <li class="thread"><span class="avatar"></span><div class="thread-text"><div class="thread-top"><b>houseofL</b><span>Jan 5</span></div><div class="thread-msg"><span>they are fantastic!</span></div></div></li>
        <li class="thread is-unread"><span class="avatar"></span><div class="thread-text"><div class="thread-top"><b>Bessie_0415</b><span>Jan 3</span></div><div class="thread-msg"><span>No problem</span><i class="unread"></i></div></div></li>
        <li class="thread"><span class="avatar"></span><div class="thread-text"><div class="thread-top"><b>jessie.rowan</b><span>Jan 2</span></div><div class="thread-msg"><span>amazing actors</span></div></div></li>
        <li class="thread"><span class="avatar"></span><div class="thread-text"><div class="thread-top"><b>spencer.wright</b><span>Jan 1</span></div><div class="thread-msg"><span>see you there</span></div></div></li>
      </ul>
      <div class="fab"><svg width="10" height="10"><path d="M2 8l1-3 4-4 2 2-4 4z" fill="#fff"/></svg></div>
    </main>
  </div>
  <footer class="nav"><span class="nav-active-mark"></span>
    <div class="nav-icons">
      <svg viewBox="0 0 12 12"><path d="M1 6L6 1l5 5v5H1z" fill="var(--blue)"/></svg>
      <svg viewBox="0 0 12 12"><circle cx="6" cy="6" r="5" fill="var(--orange)"/></svg>
      <svg viewBox="0 0 12 12"><circle cx="5" cy="5" r="4" fill="var(--blue)"/><path d="M8 8l3 3" stroke="var(--blue)" stroke-width="1.6"/></svg>
      <svg viewBox="0 0 12 12"><rect x="1" y="3" width="10" height="8" fill="var(--blue)"/><path d="M5 5l3 2-3 2z" fill="#fff"/></svg>
      <svg viewBox="0 0 12 12"><path d="M1 11l7-7 1 1-7 7z" fill="var(--blue)"/><circle cx="9.5" cy="2.5" r="1.3" fill="var(--blue)"/></svg>
    </div><span class="home-bar"></span></footer>
</article>

<!-- CHANNEL SCREEN V1 -->
<div class="screen-label" style="left:496px;top:840px">CHANNEL SCREEN V1</div>
<article class="screen" style="left:526px">
  <div class="status"><span>9:41</span>
    <span class="status-icons"><svg width="11" height="7"><rect x="0" y="5" width="2" height="2"/><rect x="3" y="3.5" width="2" height="3.5"/><rect x="6" y="2" width="2" height="5"/><rect x="9" y="0" width="2" height="7"/></svg><svg width="9" height="7"><path d="M0.5 2.5a6 6 0 0 1 8 0M2 4a4 4 0 0 1 5 0M3.5 5.5a1.6 1.6 0 0 1 2 0" stroke="#000" fill="none" stroke-width="1.1"/></svg><svg width="14" height="7"><rect x=".5" y=".5" width="12" height="6" rx="1.5" fill="none" stroke="#999"/><rect x="1.5" y="1.5" width="10" height="4" rx="1"/></svg></span></div>
  <div class="body">
    <nav class="rail">
      <div class="rail-item chat"></div>
      <div class="rail-item poster-a" role="img" aria-label="Channel poster: masked hero"></div>
      <div class="rail-item poster-b is-active" role="img" aria-label="Channel poster: police comedy cast"></div>
      <div class="rail-item poster-c" role="img" aria-label="Channel poster: fantasy series"></div>
      <div class="rail-item poster-d" role="img" aria-label="Channel poster: city drama"></div>
      <div class="rail-add">+</div>
    </nav>
    <main class="panel">
      <h1 class="panel-title">Precinct Forty-One <span class="dots">⋮</span></h1>
      <div class="banner" style="height:88px" role="img" aria-label="Cast photo of the show walking across a bridge"></div>
      <div class="search-row"><div class="search"><svg width="6" height="6"><circle cx="2.5" cy="2.5" r="2" stroke="#666" fill="none"/><path d="M4 4l2 2" stroke="#666"/></svg>Search</div><div class="add-member"><svg width="8" height="7"><circle cx="3" cy="2" r="1.6" fill="#444"/><path d="M0 7a3 3 0 0 1 6 0z" fill="#444"/></svg></div></div>
      <section class="group"><div class="group-head">INFORMATION</div>
        <div class="channel"><i class="ico-tri"></i>channel-rules</div>
        <div class="channel"><i class="ico-dot"></i>news-and-events</div></section>
      <section class="group" style="margin-top:18px"><div class="group-head">COMMUNITY</div>
        <div class="channel"><span class="hash">#</span>introduce-yourself</div>
        <div class="channel"><span class="hash">#</span>news-and-events</div>
        <div class="channel"><span class="hash">#</span>memes-and-jokes</div>
        <div class="channel"><span class="hash">#</span>best-of-det-rourke</div></section>
      <section class="group" style="margin-top:18px"><div class="group-head">VOICE CHANNELS</div>
        <div class="channel"><span class="hash">#</span>song-requests</div>
        <div class="channel"><i class="ico-vol"></i>General</div></section>
      <div class="fab"><svg width="10" height="10"><path d="M2 8l1-3 4-4 2 2-4 4z" fill="#fff"/></svg></div>
    </main>
  </div>
  <footer class="nav"><span class="nav-active-mark"></span>
    <div class="nav-icons">
      <svg viewBox="0 0 12 12"><path d="M1 6L6 1l5 5v5H1z" fill="var(--blue)"/></svg>
      <svg viewBox="0 0 12 12"><circle cx="6" cy="6" r="5" fill="var(--orange)"/></svg>
      <svg viewBox="0 0 12 12"><circle cx="5" cy="5" r="4" fill="var(--blue)"/><path d="M8 8l3 3" stroke="var(--blue)" stroke-width="1.6"/></svg>
      <svg viewBox="0 0 12 12"><rect x="1" y="3" width="10" height="8" fill="var(--blue)"/><path d="M5 5l3 2-3 2z" fill="#fff"/></svg>
      <svg viewBox="0 0 12 12"><path d="M1 11l7-7 1 1-7 7z" fill="var(--blue)"/><circle cx="9.5" cy="2.5" r="1.3" fill="var(--blue)"/></svg>
    </div><span class="home-bar"></span></footer>
</article>

<!-- CHANNEL SCREEN V2 -->
<div class="screen-label" style="left:826px;top:840px">CHANNEL SCREEN V2</div>
<article class="screen" style="left:856px">
  <div class="status"><span>9:41</span>
    <span class="status-icons"><svg width="11" height="7"><rect x="0" y="5" width="2" height="2"/><rect x="3" y="3.5" width="2" height="3.5"/><rect x="6" y="2" width="2" height="5"/><rect x="9" y="0" width="2" height="7"/></svg><svg width="9" height="7"><path d="M0.5 2.5a6 6 0 0 1 8 0M2 4a4 4 0 0 1 5 0M3.5 5.5a1.6 1.6 0 0 1 2 0" stroke="#000" fill="none" stroke-width="1.1"/></svg><svg width="14" height="7"><rect x=".5" y=".5" width="12" height="6" rx="1.5" fill="none" stroke="#999"/><rect x="1.5" y="1.5" width="10" height="4" rx="1"/></svg></span></div>
  <div class="body">
    <nav class="rail">
      <div class="rail-item chat"></div>
      <div class="rail-item poster-a" role="img" aria-label="Channel poster: masked hero"></div>
      <div class="rail-item poster-b is-active" role="img" aria-label="Channel poster: police comedy cast"></div>
      <div class="rail-item poster-c" role="img" aria-label="Channel poster: fantasy series"></div>
      <div class="rail-item poster-d" role="img" aria-label="Channel poster: city drama"></div>
      <div class="rail-add">+</div>
    </nav>
    <main class="panel">
      <div class="banner-full" role="img" aria-label="Cast photo of the show walking across a bridge"></div>
      <h1 class="panel-title" style="margin-top:10px">Precinct Forty-One <span class="dots">⋮</span></h1>
      <div class="search-row"><div class="search"><svg width="6" height="6"><circle cx="2.5" cy="2.5" r="2" stroke="#666" fill="none"/><path d="M4 4l2 2" stroke="#666"/></svg>Search</div><div class="add-member"><svg width="8" height="7"><circle cx="3" cy="2" r="1.6" fill="#444"/><path d="M0 7a3 3 0 0 1 6 0z" fill="#444"/></svg></div></div>
      <section class="group"><div class="group-head">INFORMATION</div>
        <div class="channel"><i class="ico-tri"></i>channel-rules</div>
        <div class="channel"><i class="ico-dot"></i>news-and-events</div></section>
      <section class="group" style="margin-top:18px"><div class="group-head">COMMUNITY</div>
        <div class="channel"><span class="hash">#</span>introduce-yourself</div>
        <div class="channel"><span class="hash">#</span>news-and-events</div>
        <div class="channel"><span class="hash">#</span>memes-and-jokes</div>
        <div class="channel"><span class="hash">#</span>best-of-det-rourke</div></section>
      <section class="group" style="margin-top:18px"><div class="group-head">VOICE CHANNELS</div>
        <div class="channel"><span class="hash">#</span>song-requests</div>
        <div class="channel"><i class="ico-vol"></i>General</div>
        <div class="channel"><i class="ico-vol"></i>Music</div></section>
      <div class="fab"><svg width="10" height="10"><path d="M2 8l1-3 4-4 2 2-4 4z" fill="#fff"/></svg></div>
    </main>
  </div>
  <footer class="nav"><span class="nav-active-mark"></span>
    <div class="nav-icons">
      <svg viewBox="0 0 12 12"><path d="M1 6L6 1l5 5v5H1z" fill="var(--blue)"/></svg>
      <svg viewBox="0 0 12 12"><circle cx="6" cy="6" r="5" fill="var(--orange)"/></svg>
      <svg viewBox="0 0 12 12"><circle cx="5" cy="5" r="4" fill="var(--blue)"/><path d="M8 8l3 3" stroke="var(--blue)" stroke-width="1.6"/></svg>
      <svg viewBox="0 0 12 12"><rect x="1" y="3" width="10" height="8" fill="var(--blue)"/><path d="M5 5l3 2-3 2z" fill="#fff"/></svg>
      <svg viewBox="0 0 12 12"><path d="M1 11l7-7 1 1-7 7z" fill="var(--blue)"/><circle cx="9.5" cy="2.5" r="1.3" fill="var(--blue)"/></svg>
    </div><span class="home-bar"></span></footer>
</article>

</body>
</html>
```